Flyer to promote new Commercial HVAC Preventative Maintenance clients

This flyer will be in the body of emails that will be sent to new, existing, and/or potential commericial buildings HVAC clients. It will have the least amount of words used, but it will convey the point with pertinent pictorial and graphics. It will show the value of a Periodic/Preventative routine maintenance to lower operating costs of their commericial buildings (i.e. office, medical, shopping centers, apartment, warehouse facility, etc.), in the following ways:
1) Reduce monthly power usage,
2) Reduce emergency HVAC service calls,
3) Reduce costly repairs costs,
4) Reduce HVAC down-times and angry tenants,
5) Increases the life expectancy of the existing and/or new HVAC equipment in the building and/or the equipment's' early replacement costs,
6) Reduces tenant's early termination of their lease and law suits against the landlords,
7) Increases tenant's renewal of the lease and agree to pay the increase rental rates,
8) Reduces unhappy customers and increases tenant's productivity,
9) By reducing the landlord's expenses, the value of the property will increase considerably and profitable to sell their holdings, or refinance and keep their holdings with an increased ROI (Return On Investment).

Landlords can not depend on their tenants' obligation to maintain the landlords' major assets, which is their HVAC equipment and systems.

With the periodic maintenance done by one reliable and licensed HVAC company, the will not use different companies that may or may not do the right repair job on their unit and hurt their bottom line and increase HVAC replacement COSTLY rates.

```html
<!DOCTYPE html>
<html lang="en">
<head>
<meta charset="utf-8">
<title>HVAC Routine Preventative Maintenance Program</title>
<link href="https://fonts.googleapis.com/css2?family=Roboto:wght@300;400;500;700;900&display=swap" rel="stylesheet">
<style>
:root{
  --page:#eaf3f7;
  --white:#ffffff;
  --ink:#111111;
  --muted:#6b6f73;
  --body:#3a3d40;
  --sky:#00b4e6;
  --orange:#f15a22;
  --orange-light:#f7a21b;
  --blue-light:#27d0f5;
  --blue-deep:#0a8fd6;
  --border:#d7dde1;
}
*{margin:0;padding:0;box-sizing:border-box}
html,body{width:1200px;height:4911px;overflow:hidden}
body{position:relative;background:var(--page);font-family:'Roboto',sans-serif;color:var(--ink)}
.hero{position:absolute;left:0;top:0;width:1200px;height:809px;background:linear-gradient(90deg,#ffffff 0%,#f7f9fb 45%,#eef2f5 100%)}
.hero-photo{position:absolute;left:640px;top:128px;width:560px;height:681px;background:linear-gradient(90deg,rgba(238,242,245,0) 0%,#cfd8df 30%,#b7c3cc 60%,#dfe6ea 100%)}
.topband{position:absolute;left:0;top:0}
.logo{position:absolute;left:108px;top:104px;display:flex;align-items:center;gap:16px}
.logo-dot{width:30px;height:30px;border-radius:50%;background:var(--orange)}
.logo-name{font-weight:500;font-size:46px;color:#6a6e72;letter-spacing:-0.5px}
.call{position:absolute;left:734px;top:20px;display:flex;align-items:center;gap:20px;color:var(--white)}
.call svg{flex:none}
.call-text{font-weight:700;font-size:36px;line-height:44px}
.hero-title{position:absolute;left:97px;top:272px;font-weight:900;font-size:57px;line-height:71px;color:var(--ink);text-transform:uppercase;letter-spacing:0.3px}
.btn{position:absolute;left:95px;top:582px;width:225px;height:90px;border-radius:45px;background:var(--orange);color:var(--white);font-weight:700;font-size:24px;display:flex;align-items:center;justify-content:center}
.card{position:absolute;left:92px;width:1015px;background:var(--white);border:4px solid var(--border)}
.photo{position:absolute;top:-4px;bottom:-4px;width:359px}
.card.left .photo{left:-4px}
.card.right .photo{right:-4px}
.copy{position:absolute}
.card.left .copy{left:457px;width:525px}
.card.right .copy{left:57px;width:500px}
.copy h2{font-weight:500;font-size:33px;line-height:43px;color:var(--ink);margin-bottom:28px}
.copy p{font-weight:400;font-size:26px;line-height:44px;color:var(--muted)}
.icon{position:absolute;width:152px;height:152px;border-radius:50%;background:var(--white);display:flex;align-items:center;justify-content:center}
.icon-core{width:134px;height:134px;border-radius:50%;display:flex;align-items:center;justify-content:center}
.icon-core.warm{background:linear-gradient(180deg,var(--orange-light),var(--orange))}
.icon-core.cool{background:linear-gradient(180deg,var(--blue-light),var(--blue-deep))}
.summary{position:absolute;left:92px;top:3768px;width:1015px;text-align:center;font-weight:400;font-size:33px;line-height:61px;color:var(--body)}
.note{position:absolute;left:130px;top:4310px;width:940px;text-align:center;font-weight:400;font-size:33px;line-height:61px;color:var(--body)}
.footer{position:absolute;left:0;top:4713px;width:1200px;height:198px;background:var(--sky);color:var(--white);text-align:center;font-size:29px;line-height:48px;padding-top:70px}
</style>
</head>
<body>
<section class="hero">
  <div class="hero-photo" role="img" aria-label="Row of outdoor air conditioning condenser units"></div>
  <svg class="topband" width="1200" height="250" viewBox="0 0 1200 250">
    <polygon points="590,0 1200,0 1200,128 515,128" fill="#00b4e6"/>
    <ellipse cx="250" cy="20" rx="330" ry="218" fill="#ffffff"/>
  </svg>
  <div class="logo"><span class="logo-dot"></span><span class="logo-name">nova crest</span></div>
  <div class="call">
    <svg width="64" height="64" viewBox="0 0 64 64"><circle cx="32" cy="32" r="30" fill="#ffffff"/><path d="M22 16c2 0 4 5 5 8 1 2-3 4-2 6 2 4 5 7 9 9 2 1 4-3 6-2 3 1 8 3 8 5 0 4-4 7-8 7-14-1-26-13-27-27 0-4 4-6 9-6z" fill="#00b4e6"/></svg>
    <div class="call-text">CALL US<br>(555)014-2870</div>
  </div>
  <h1 class="hero-title">Enroll in our HVAC<br>Routine Preventative<br>Maintenance RPM<br>Program</h1>
  <div class="btn">BENEFITS</div>
</section>

<article class="card left" style="top:740px;height:416px">
  <div class="photo" role="img" aria-label="Technician servicing an outdoor condenser unit" style="background:linear-gradient(135deg,#8fa3b4,#3f5a7a 60%,#2b3f5a)"></div>
  <div class="copy" style="top:64px">
    <h2>Priority Service<br>Response</h2>
    <p>During busy seasons when you most depend on quick response, you will be scheduled on PRIORITY. Our professional technical team will handle your HVAC</p>
  </div>
</article>
<div class="icon" style="left:370px;top:872px"><div class="icon-core warm"><svg width="70" height="70" viewBox="0 0 70 70" fill="none" stroke="#fff" stroke-width="4"><rect x="10" y="40" width="50" height="18" rx="3"/><path d="M22 40V18M16 18h12M48 40V14l-6-4M48 14l6-4"/></svg></div></div>

<article class="card right" style="top:1185px;height:547px">
  <div class="photo" role="img" aria-label="Engineer checking an electrical control panel" style="background:linear-gradient(160deg,#c9cfd4,#8e979e 55%,#4d555c)"></div>
  <div class="copy" style="top:64px">
    <h2>Reduce Monthly<br>Power Usage</h2>
    <p>HVAC energy consumptions accounts for 40% to 60% of commercial building’s total energy use. Clean coils and filters, lubricated motors, and smooth-running HVAC equipment, which are the result of a well-maintained system, WILL REDUCE YOUR COSTLY ENERGY WASTE.</p>
  </div>
</article>
<div class="icon" style="left:676px;top:1387px"><div class="icon-core cool"><svg width="70" height="70" viewBox="0 0 70 70" fill="none" stroke="#fff" stroke-width="4"><rect x="20" y="8" width="30" height="54" rx="5"/><path d="M38 20l-8 16h10l-8 16"/></svg></div></div>

<article class="card left" style="top:1769px;height:471px">
  <div class="photo" role="img" aria-label="Technician working on a wall-mounted unit" style="background:linear-gradient(135deg,#a9b7c4,#4d6c96 55%,#2a4878)"></div>
  <div class="copy" style="top:66px">
    <h2>Bring HVAC Repairs<br>Costs to a MINIMUM</h2>
    <p>Our pro-team of technicians will prevent foreseeable failures, therefore reduce expensive repairs and changeouts, and in most cases prevent future emergency service calls,</p>
  </div>
</article>
<div class="icon" style="left:370px;top:1901px"><div class="icon-core warm"><svg width="70" height="70" viewBox="0 0 70 70" fill="none" stroke="#fff" stroke-width="4"><circle cx="35" cy="20" r="12"/><path d="M35 13v14M31 17h6M31 23h6M14 62V44l-6 6M14 44l6 6M35 62V42M56 62V44l-6 6M56 44l6 6"/></svg></div></div>

<article class="card right" style="top:2272px;height:407px">
  <div class="photo" role="img" aria-label="Technician testing a condenser with pressure gauges" style="background:linear-gradient(160deg,#e6e9ec,#b9c0c6 55%,#7d868d)"></div>
  <div class="copy" style="top:64px">
    <h2>OEM Parts IN STOCK*</h2>
    <p>We stock more OEM (Original Equipment Manufacturer) parts than any of our local competitors, which gets your system up and running again MUCH FASTER.</p>
  </div>
</article>
<div class="icon" style="left:676px;top:2401px"><div class="icon-core cool"><svg width="70" height="70" viewBox="0 0 70 70" fill="none" stroke="#fff" stroke-width="4"><path d="M35 12L60 56H10Z"/><path d="M35 28v14"/><circle cx="35" cy="49" r="2" fill="#fff"/></svg></div></div>

<article class="card left" style="top:2711px;height:472px">
  <div class="photo" role="img" aria-label="Hand holding a phone with a smart thermostat app" style="background:linear-gradient(135deg,#dfe4e8,#9fb3c6 55%,#3b5f8f)"></div>
  <div class="copy" style="top:68px">
    <h2>Reduce HVAC<br>Down Times</h2>
    <p>A truly well-maintained system will prolong proper operation of the equipment and optimizes performance and healthy long life of all parts of the system and minimize breakdowns.</p>
  </div>
</article>
<div class="icon" style="left:370px;top:2843px"><div class="icon-core warm"><svg width="70" height="70" viewBox="0 0 70 70" fill="none" stroke="#fff" stroke-width="4"><rect x="8" y="12" width="54" height="22" rx="3"/><path d="M14 26h42"/><circle cx="24" cy="50" r="10"/><path d="M24 40v20M14 50h20M44 44c3 3-3 6 0 9s-3 6 0 9M54 44c3 3-3 6 0 9"/></svg></div></div>

<article class="card right" style="top:3215px;height:445px">
  <div class="photo" role="img" aria-label="Rooftop commercial HVAC units under a clear sky" style="background:linear-gradient(180deg,#cfe3f2,#aab6c0 60%,#6f7880)"></div>
  <div class="copy" style="top:68px">
    <h2>Increase Your Productivity</h2>
    <p>Your clients and team of employees expect a comfortable environment. A year-round dependable HVAC upkeep assures repeat business and escalates productivity of your team.</p>
  </div>
</article>
<div class="icon" style="left:676px;top:3345px"><div class="icon-core cool"><svg width="70" height="70" viewBox="0 0 70 70" fill="none" stroke="#fff" stroke-width="4"><path d="M30 24L46 10l16 14M34 22v20h24V22"/><rect x="42" y="30" width="8" height="8"/><circle cx="20" cy="40" r="8"/><path d="M6 62c0-8 6-12 14-12s14 4 14 12"/></svg></div></div>

<p class="summary">With our unique Routine Preventative Maintenance (RPM) program performed by our team of expert technicians, backed by NOVA Crest Heating &amp; Air Conditioning, a 45-year licensed HVAC company, you will no longer wish to use different companies that use unconventional repairs to only ruin your expensive HVAC equipment. Your units will be optimized and ready to perform efficiently and live their full life expectancy and SIGNIFICANTLY REDUCE COSTLY EARLY REPLACEMENTS.</p>

<p class="note">*NOVA Crest has access to OEM parts for the following major brands: Carvell, Brayden, Paxley, Allied Standard, Tramont, Yorvik, Lenmark, CoolPro, Goodwell, Dairon, Rhemco, Ruvell, Amaro, Mitsuka. And families of ICS (Integrated Comfort Systems).</p>

<footer class="footer">© 2023 Nova Crest Heating &amp; Air Conditioning.<br>All rights reserved.Privacy&nbsp; |&nbsp; Terms of Use</footer>
</body>
</html>
```